Contest - label design for a health related product

Velmora is a brand for a set of 4 different colloids, namely colloidal silver, colloidal gold, colloidal zinc and colloidal copper. These colloids have a positive impact on peopleā€˜s health. Each colloid has different impacts on the health.

A colloid is a substance microscopically dispersed evenly throughout another substance. In our case the substance is water and a metal which has been broken down by an electrochemical process to the smallest possible particle size (also called nano-particles). Please google "colloidal silver".

Your job is to design a label (70 mm high x 132 mm wide) for each of the 4 types of colloids. The label will be printed as a sticker which then in return will be placed on a bottle made out of brown glass (see attachment). The 4 labels should have the respective logo (see attachments) and colors that represent the respective type of colloid, i.e. for colloidal silver, there should be a silverish color used as a theme on the label and so on. You should first create one label for colloidal silver. If we like the design we will select you and then you can make the 3 remaining labels with the respective color and logo.

What information goes on the label:

On the left side there will be text and a graphic of a bar code:
Distribution through
Quill Company
Address
Postal Code City
Country

A graphic of a bar code

Made in Austria
Copyright by Harvex company, registration no. 804172,

In the middle:
The logo (see attachment)
The product, i.e. "Kolloidales Silber" (it's in German)
The concentration in ppm, i.e. 25 ppm
The amount in ml, i.e. 500 ml

On the right side:
Store in a cold place and away from electrical fields, including the refrigerator and the micro wave. Do not immerse any metal objects into the colloid, such as a metal table spoon.

Ingredients: Aqua bidest. and nano particles of silver.

We have attached a label that we found on Plotfair. We like the colors and the style.

We need the file in illustrator with editable fonts.

As soon as we have designs from 10 different designers, we will guarantee the project!
Updates

Dear All,

First of all, we would like to thank everyone who participated in this project. It was a very difficult decision as there were a lot of top designs. You guys are incredibly creative.

Thank you and all the best for 2013! Keep on the good jobs you guys are doing.

Target Market(s)

Health concious people between 25 and 70

Industry/Entity Type

Electrical

Requirements
Must have
• - the attached logos (1 for each type of colloid)
- clear
- vivid colors, matching the logo
- minimalistic
- abstract
Should not have
• - Heavy, dark colors
- Text that hints to health benefits (just use the text we have given you)

```html
<!DOCTYPE html>
<html lang="en">
<head>
<meta charset="utf-8">
<title>Velmora – Kolloidales Silber label</title>
<link rel="stylesheet" href="https://fonts.googleapis.com/css2?family=Anton&family=Arimo:wght@400;700&family=Roboto+Condensed:wght@400;700&display=swap">
<style>
  :root {
    --tan: #c1955a;
    --tan-light: #e3c9a3;
    --teal: #1a9e9a;
    --blue: #2aa6d0;
    --blue-deep: #1b82b8;
    --brand-blue: #2e78b8;
    --ink: #111111;
    --white: #ffffff;
    --amber: #7a3f12;
  }
  * { margin: 0; padding: 0; box-sizing: border-box; }
  html, body { width: 1200px; height: 927px; overflow: hidden; background: var(--white); }
  .canvas { position: relative; width: 1200px; height: 927px; }

  .label {
    position: absolute; left: 50px; top: 90px; width: 922px; height: 556px;
    overflow: hidden; background: var(--white);
  }
  .label-art { position: absolute; inset: 0; }

  .brand-tab {
    position: absolute; left: 348px; top: 0; width: 215px; height: 134px;
    border-radius: 0 0 18px 18px;
    background: linear-gradient(180deg, var(--tan-light), var(--tan));
    border: 3px solid #a87a40; border-top: none;
    display: flex; align-items: center; justify-content: center;
  }
  .brand-dot { width: 54px; height: 54px; border-radius: 50%; background: var(--white); opacity: .85; }

  .distribution {
    position: absolute; left: 10px; top: 135px; width: 255px;
    text-align: center; font: 400 23px/1.03 "Arimo", sans-serif; color: var(--ink);
  }
  .distribution strong { font-weight: 700; }

  .code-box {
    position: absolute; left: 43px; top: 315px; width: 179px; height: 102px;
    background: var(--white); border: 1px solid #8a8a8a;
  }

  .imprint {
    position: absolute; left: 20px; top: 440px; width: 225px;
    text-align: center; font: 400 16px/1.3 "Roboto Condensed", sans-serif; color: var(--white);
  }

  .brand-name {
    position: absolute; left: 300px; top: 148px; width: 310px; text-align: center;
    font: 400 32px/1 "Arimo", sans-serif; color: var(--brand-blue);
  }
  .product-name {
    position: absolute; left: 300px; top: 192px; width: 310px; text-align: center;
    font: 400 64px/1.06 "Anton", sans-serif; color: var(--ink);
  }
  .volume {
    position: absolute; left: 300px; top: 348px; width: 310px; text-align: center;
    font: 700 31px/1 "Roboto Condensed", sans-serif; color: var(--brand-blue);
  }

  .storage-note {
    position: absolute; left: 655px; top: 20px; width: 240px; text-align: center;
    font: 400 17.5px/1.18 "Arimo", sans-serif; color: var(--white);
  }
  .ingredients {
    position: absolute; left: 680px; top: 305px; width: 230px; text-align: center;
    font: 400 19px/1.2 "Arimo", sans-serif; color: var(--ink);
  }
  .concentration {
    position: absolute; left: 755px; top: 490px; width: 130px; text-align: center;
    font: 700 29px/1 "Roboto Condensed", sans-serif; color: var(--white);
  }

  .bottle-preview {
    position: absolute; left: 1002px; top: 445px; width: 138px; height: 428px;
    border-radius: 22px 22px 14px 14px;
    background: linear-gradient(90deg, #5a2a08, var(--amber) 45%, #4a2006);
  }
</style>
</head>
<body>
<main class="canvas">
  <section class="label">
    <svg class="label-art" viewBox="0 0 922 556" preserveAspectRatio="none" aria-hidden="true">
      <defs>
        <linearGradient id="top-wash" x1="0" y1="0" x2="0" y2="1">
          <stop offset="0" stop-color="#c89c62"/>
          <stop offset="0.55" stop-color="#f3e6d4"/>
          <stop offset="1" stop-color="#ffffff"/>
        </linearGradient>
        <linearGradient id="sea" x1="0" y1="0" x2="1" y2="1">
          <stop offset="0" stop-color="#1fa3c6"/>
          <stop offset="1" stop-color="#1b86bc"/>
        </linearGradient>
      </defs>
      <rect x="0" y="0" width="922" height="170" fill="url(#top-wash)"/>
      <path d="M621,0 L922,0 L922,250 C780,252 650,210 622,80 Z" fill="#c1955a"/>
      <path d="M0,262 C220,230 460,300 922,352 L922,556 L0,556 Z" fill="#1a9e9a"/>
      <path d="M0,300 C230,268 480,360 922,392 L922,556 L0,556 Z" fill="#bfe6ea"/>
      <path d="M0,335 C240,305 520,420 922,418 L922,556 L0,556 Z" fill="url(#sea)"/>
    </svg>

    <div class="brand-tab"><span class="brand-dot"></span></div>

    <p class="distribution">Distribution through<br><strong>Quill Company</strong><br>Address<br>Postal Code City<br>Country</p>
    <div class="code-box"></div>
    <p class="imprint">Made in Austria<br>Copyright by<br>Harvex Company,<br>Registration No. 804172,</p>

    <p class="brand-name">Velmora Kupfer</p>
    <h1 class="product-name">Kolloidales<br>Silber</h1>
    <p class="volume">500 ml</p>

    <p class="storage-note">Store in a cold place and away from electrical fields, including the refrigerator and the micro wave. Do not immerse any metal objects into the colloid, such as a metal table spoon.</p>
    <p class="ingredients">Ingredients:<br>Aqua bidest and<br>nano particles of silver.</p>
    <p class="concentration">25 ppm</p>
  </section>

  <div class="bottle-preview" role="img" aria-label="Brown glass bottle with the label applied"></div>
</main>
</body>
</html>
```